Creative Photography Business Card

Looking for a unique, creative, elegant, sophisticated and professional business card for my photography business.

I specialise in children, families, modelling, weddings and special event photography

Things to include:
Logo - will attach
Email: hello@mirabellwoodsphoto.com.au
web:www.mirabellwoodsphoto.com.au
Ph: 0438 502 671

I will also upload some of my work that you may like to use.

Please be creative and unique in your designs.

```html
<!DOCTYPE html>
<html lang="en">
<head>
<meta charset="utf-8">
<title>Mirabell Woods Photography – Business Card</title>
<link href="https://fonts.googleapis.com/css2?family=Oswald:wght@400;500&display=swap" rel="stylesheet">
<style>
  :root {
    --backdrop: #e9e9e9;
    --card-black: #222222;
    --ribbon-orange: #e49f2e;
    --badge-cream: #ecebe8;
    --badge-blue: #3b6ea6;
    --contact-orange: #e9a12f;
  }
  * { box-sizing: border-box; margin: 0; padding: 0; }
  html, body { width: 1200px; height: 900px; overflow: hidden; }
  body { background: var(--backdrop); position: relative; font-family: "Oswald", sans-serif; }

  .card {
    position: absolute; top: 127px; width: 327px; height: 610px;
    background: var(--card-black); border-radius: 16px; overflow: hidden;
  }
  .card--front { left: 300px; }
  .card--back { left: 710px; }

  .ribbon-band { position: absolute; left: 97px; top: 0; width: 133px; height: 100%; background: var(--ribbon-orange); }
  .ribbon-tail { position: absolute; left: 97px; top: 0; }

  .badge {
    position: absolute; border-radius: 50%; background: var(--badge-cream);
    display: flex; flex-direction: column; align-items: center; justify-content: center;
    color: var(--badge-blue); font-weight: 500; text-align: center; line-height: 1.05;
  }
  .badge--front { left: 48px; top: 190px; width: 230px; height: 230px; font-size: 34px; }
  .badge--back { left: 71px; top: 59px; width: 184px; height: 184px; font-size: 27px; }
  .badge__sub { font-size: 0.42em; letter-spacing: 0.18em; margin-top: 8px; }

  .contact { position: absolute; left: 36px; width: 254px; text-align: center; color: var(--contact-orange); }
  .contact__phone { top: 346px; font-size: 31px; font-weight: 500; letter-spacing: 0.02em; }
  .contact__rule { position: absolute; left: 36px; width: 254px; height: 2px; background: var(--contact-orange); }
  .contact__rule--top { top: 388px; }
  .contact__rule--bottom { top: 447px; }
  .contact__line { font-size: 15.5px; text-transform: uppercase; letter-spacing: 0.01em; }
  .contact__email { top: 394px; }
  .contact__web { top: 418px; }

  .portfolio {
    position: absolute; left: 36px; top: 451px; width: 254px; height: 132px;
    display: grid; grid-template-columns: 84px 84px 32px 50px; grid-template-rows: 1fr 1fr; gap: 2px;
  }
  .portfolio__shot:nth-child(1) { background: linear-gradient(135deg, #8b806d, #b9ad95); }
  .portfolio__shot:nth-child(2) { background: linear-gradient(135deg, #c9b64a, #6c8a3c); }
  .portfolio__shot:nth-child(3) { background: linear-gradient(135deg, #b8a57b, #8e8a55); }
  .portfolio__shot:nth-child(4) { background: linear-gradient(135deg, #5d4736, #b74a3f); }
  .portfolio__shot:nth-child(5) { background: linear-gradient(135deg, #cbbba8, #8a7a68); }
  .portfolio__shot:nth-child(6) { background: linear-gradient(135deg, #6f8a4c, #a99f82); }
  .portfolio__shot:nth-child(7) { background: linear-gradient(135deg, #d7a1a8, #7c9a6a); grid-column: span 2; }
</style>
</head>
<body>

  <section class="card card--front" aria-label="Business card front">
    <div class="ribbon-band"></div>
    <div class="badge badge--front">
      <span>Mirabell<br>Woods</span>
      <span class="badge__sub">PHOTOGRAPHY</span>
    </div>
  </section>

  <section class="card card--back" aria-label="Business card back">
    <svg class="ribbon-tail" width="133" height="330" viewBox="0 0 133 330" aria-hidden="true">
      <polygon points="0,0 133,0 133,328 66.5,261 0,328" fill="var(--ribbon-orange)"/>
    </svg>
    <div class="badge badge--back">
      <span>Mirabell<br>Woods</span>
      <span class="badge__sub">PHOTOGRAPHY</span>
    </div>

    <p class="contact contact__phone">0438 502 671</p>
    <div class="contact__rule contact__rule--top"></div>
    <p class="contact contact__line contact__email">hello@mirabellwoodsphoto.com.au</p>
    <p class="contact contact__line contact__web">www.mirabellwoodsphoto.com.au</p>
    <div class="contact__rule contact__rule--bottom"></div>

    <div class="portfolio">
      <div class="portfolio__shot" role="img" aria-label="Sepia portrait of children lying on the grass"></div>
      <div class="portfolio__shot" role="img" aria-label="Portrait of a smiling girl against a painted backdrop"></div>
      <div class="portfolio__shot" role="img" aria-label="Outdoor portrait of a child in a field"></div>
      <div class="portfolio__shot" role="img" aria-label="Portrait of a girl in red by a tree"></div>
      <div class="portfolio__shot" role="img" aria-label="Portrait of a young woman resting on her hands"></div>
      <div class="portfolio__shot" role="img" aria-label="Family portrait outdoors"></div>
      <div class="portfolio__shot" role="img" aria-label="Three sisters smiling together"></div>
    </div>
  </section>

</body>
</html>
```